Awesome Web Design Project

must have a link to mingleton of the homepage preferably a scrolling view of our mingleton page!

We are an exciting new electrical company with a strong focus on energy efficiency and offering the latest technologies.

The design should allow easy navigation, there shouldn't be too many menus, It should look clean and sleek, Colours to consider could be green, silver/chrome, black,

The site should convey technology, efficiency and simplicity

Must be viewable on all devices, pc's, tablets, phones ie Responsive
Updates

Logo and some pics uploaded!

Industry/Entity Type

Electrical

Requirements
Must have
• must include the following pages,
about us
our services
gallery
contact us
Connect with us
Nice to have
• Would be great if the website design used a user friendly cms,
Should not have
• too many links, menus, clutter it should be clean and easy to navigate

```html
<!DOCTYPE html>
<html lang="en">
<head>
<meta charset="utf-8">
<title>Volta Lane Electrical</title>
<link href="https://fonts.googleapis.com/css2?family=Oswald:wght@400;500&family=Open+Sans:wght@400;600;700&display=swap" rel="stylesheet">
<style>
:root{
  --lime:#d6df22;
  --ink:#1b1b1b;
  --grey-text:#555;
  --nav-text:#444;
  --page:#ececec;
  --white:#fff;
  --social:#3b5998;
  --arrow:#8a8a8a;
  --rule:#dcdcdc;
}
*{box-sizing:border-box;margin:0;padding:0}
html,body{width:1200px;height:900px;overflow:hidden}
body{background:var(--page);font-family:"Open Sans",sans-serif;position:relative}
.hero{position:absolute;left:0;top:0;width:1200px;height:652px;
  background:radial-gradient(ellipse 420px 300px at 600px 400px,#8a8a8a 0%,#3e3e3e 45%,#141414 100%);}
.hero-photo{position:absolute;inset:0}
.site-header{position:absolute;left:16px;top:32px;width:1170px;height:60px;background:var(--white);display:flex;align-items:center}
.brand{display:flex;align-items:center;gap:10px;margin-left:22px;width:440px}
.brand-mark{width:30px;height:30px;background:var(--lime)}
.brand-name{font-family:"Oswald",sans-serif;font-size:24px;color:#2d3a3f;letter-spacing:1px;text-transform:uppercase}
.main-nav{display:flex;height:100%;margin-left:auto}
.main-nav a{font-family:"Oswald",sans-serif;font-size:18px;color:var(--nav-text);text-decoration:none;display:flex;align-items:center;text-transform:uppercase}
.nav-about{margin-right:43px}
.nav-services{margin-right:46px}
.nav-services::after{content:"";border:4px solid transparent;border-top-color:var(--nav-text);margin:4px 0 0 6px}
.nav-gallery{margin-right:54px}
.nav-contact{margin-right:15px}
.connect{background:var(--lime);width:171px;justify-content:center;font-family:"Open Sans",sans-serif!important;font-weight:700;font-size:16px!important;color:#1e3d52!important}
.social{background:var(--social);width:62px;justify-content:center;font-family:"Open Sans",sans-serif!important;font-size:11px!important;color:var(--white)!important;text-transform:none!important}
.slider-arrow{position:absolute;top:343px;width:55px;height:58px;background:var(--arrow);opacity:.85;display:flex;align-items:center;justify-content:center}
.arrow-prev{left:0}.arrow-next{right:0}
.hero-copy{position:absolute;left:300px;top:330px;width:600px;text-align:center;color:var(--white)}
.hero-title{font-family:"Oswald",sans-serif;font-weight:400;font-size:68px;line-height:80px;text-transform:uppercase}
.hero-title span{color:var(--lime)}
.hero-lead{font-family:"Oswald",sans-serif;font-size:19px;line-height:24px;text-transform:uppercase;margin:12px 12px 0}
.hero-more{display:inline-block;margin-top:22px;background:var(--lime);color:var(--ink);font-family:"Oswald",sans-serif;font-size:15px;width:80px;height:26px;line-height:26px;text-decoration:none}
.card{position:absolute;top:610px;width:366px;height:300px;background:var(--white);border:1px solid #d8d8d8}
.card-who{left:16px}.card-offer{left:416px;top:609px}.card-tech{left:819px}
.card-photo{position:absolute;left:3px;top:3px;width:358px;height:187px}
.photo-room{background:linear-gradient(180deg,#9c9c9c,#6f6f6f 60%,#bcbcbc)}
.photo-bulb{background:radial-gradient(circle at 240px 110px,#f4ffd0 0,#a8d400 18%,#5f9300 55%,#3e6a00 100%)}
.card-label{position:absolute;left:3px;top:143px;width:158px;height:47px;background:rgba(25,25,25,.85);color:var(--white);font-family:"Oswald",sans-serif;font-size:21px;line-height:47px;padding-left:18px;text-transform:uppercase}
.tech-label{position:absolute;left:20px;top:115px;color:var(--white);font-family:"Oswald",sans-serif;text-transform:uppercase;line-height:32px}
.tech-label b{display:block;font-weight:400;font-size:34px}
.tech-label span{display:block;font-size:27px}
.card-text{position:absolute;left:12px;right:12px;top:205px;font-size:13.4px;line-height:20px;color:var(--grey-text);text-align:justify}
.offer-title{font-family:"Oswald",sans-serif;font-weight:400;font-size:19px;color:#666;height:55px;line-height:55px;padding-left:20px;border-bottom:1px solid #e2e2e2;text-transform:uppercase}
.offer-list{list-style:none;margin:6px 12px 0 24px}
.offer-list li{font-size:15.5px;color:#444;height:32.5px;line-height:32px;border-bottom:1px dotted var(--rule);padding-left:30px;position:relative}
.offer-list li::before{content:"";position:absolute;left:0;top:15px;width:11px;height:3px;background:var(--lime)}
</style>
</head>
<body>
<section class="hero">
  <div class="hero-photo" role="img" aria-label="Row of hanging light bulbs on a dark background, the centre bulb glowing"></div>
  <div class="slider-arrow arrow-prev"><svg width="18" height="26" viewBox="0 0 18 26"><path d="M15 2 L4 13 L15 24" fill="none" stroke="#111" stroke-width="5"/></svg></div>
  <div class="slider-arrow arrow-next"><svg width="18" height="26" viewBox="0 0 18 26"><path d="M3 2 L14 13 L3 24" fill="none" stroke="#111" stroke-width="5"/></svg></div>
  <div class="hero-copy">
    <h1 class="hero-title">Innovation <span>Expert</span></h1>
    <p class="hero-lead">Lorem Ipsum is simply dummy text of the printing and typesetting industry. Lorem Ipsum has been the industry's standard dummy text ever since the 1500s,</p>
    <a class="hero-more" href="#">More</a>
  </div>
</section>

<header class="site-header">
  <div class="brand"><span class="brand-mark"></span><span class="brand-name">Volta Lane Electrical</span></div>
  <nav class="main-nav">
    <a class="nav-about" href="#">About Us</a>
    <a class="nav-services" href="#">Our Services</a>
    <a class="nav-gallery" href="#">Gallery</a>
    <a class="nav-contact" href="#">Contact Us</a>
    <a class="connect" href="#">CONNECT WITH US</a>
    <a class="social" href="#">mingleton</a>
  </nav>
</header>

<article class="card card-who">
  <div class="card-photo photo-room" role="img" aria-label="Living room with a wall-mounted TV and speakers on a brick wall"></div>
  <div class="card-label">Who We Are</div>
  <p class="card-text">Lorem Ipsum is simply dummy text of the printing and typesetting industry. Lorem Ipsum has been the industry's standard dummy text ever since the 1500s, when an unknown printer took a galley of type and scrambled it.</p>
</article>

<article class="card card-offer">
  <h2 class="offer-title">What We Offer ?</h2>
  <ul class="offer-list">
    <li>Residential / Commercial / Industrial</li>
    <li>Office / Lot Lighting</li>
    <li>Pools / Hot tubs / Spas</li>
    <li>Ceiling Fans / Lights</li>
    <li>Security Lighting</li>
    <li>Basement Wiring</li>
    <li>Office / Lot Lighting</li>
  </ul>
</article>

<article class="card card-tech">
  <div class="card-photo photo-bulb" role="img" aria-label="Glowing light bulb hanging over green grass"></div>
  <div class="tech-label"><b>New</b><span>Technologies</span></div>
  <p class="card-text">Lorem Ipsum is simply dummy text of the printing and typesetting industry. Lorem Ipsum has been the industry's standard dummy text ever since the 1500s, when an unknown printer took a galley of type and scrambled it.</p>
</article>
</body>
</html>
```